washable paper bags and accessories

We are three sisters who have discovered a mutual love of bags made from washable paper. It is a brand new business venture for bags, handbags, cosmetic bags, and home storage solutions and décor all made with washable paper.
We would like to have white crumpled paper as a background for both sides. Front of card with the words "wild plum folk" only in "bohemian typewriter regular" font. Back of card with appointment style format for our next pop up stall
Target Market(s)
mums, females
Industry/Entity Type
Business
Contact Information for Business Card
ph: 0491285364
email:wildplumfolk@postnestmail.net

```html
<!DOCTYPE html>
<html lang="en">
<head>
<meta charset="utf-8">
<title>wild plum folk – business cards</title>
<link rel="stylesheet" href="https://fonts.googleapis.com/css2?family=Almendra:wght@400&family=Roboto:wght@500;700&display=swap">
<style>
  :root {
    --stage: #ececec;
    --paper-light: #fafafa;
    --paper-mid: #e6e6e6;
    --paper-crease: rgba(0,0,0,0.07);
    --accent-red: #d8080c;
    --ink: #1c1c1c;
    --white: #ffffff;
  }
  * { box-sizing: border-box; margin: 0; padding: 0; }
  html, body {
    width: 1200px; height: 993px; overflow: hidden;
    background: var(--stage);
  }
  .canvas { position: relative; width: 1200px; height: 993px; }

  .card {
    position: absolute; width: 600px; height: 366px;
    overflow: hidden;
    box-shadow: 0 6px 18px rgba(0,0,0,0.12);
  }
  .card-texture {
    position: absolute; inset: 0;
    background:
      radial-gradient(ellipse at 22% 72%, var(--paper-crease), transparent 50%),
      radial-gradient(ellipse at 78% 24%, var(--paper-crease), transparent 45%),
      radial-gradient(ellipse at 60% 85%, rgba(0,0,0,0.04), transparent 40%),
      linear-gradient(135deg, var(--paper-light), var(--paper-mid));
  }

  /* Back: appointment side */
  .card-back { left: 80px; top: 80px; }
  .appointment-title {
    position: absolute; top: 24px; left: 0; width: 100%;
    text-align: center;
    font-family: "Almendra", serif; font-weight: 400; font-size: 40px;
    color: var(--accent-red);
  }
  .field {
    position: absolute; display: flex; align-items: flex-end;
    font-family: "Roboto", sans-serif; font-weight: 700; font-size: 17px;
    color: var(--ink);
  }
  .field-line {
    display: block; height: 2px; background: var(--ink);
    margin-left: 4px; margin-bottom: 4px;
  }
  .field-name { left: 56px; top: 132px; }
  .field-name .field-line { width: 470px; }
  .field-at { left: 116px; top: 186px; }
  .field-at .field-line { width: 318px; }
  .field-at .meridiem { margin-left: 4px; font-weight: 500; font-size: 15px; }
  .field-on { left: 160px; top: 240px; }
  .field-on .field-line { width: 376px; }

  .contact-band {
    position: absolute; left: 0; top: 290px; width: 100%; height: 52px;
    background: var(--accent-red);
    display: flex; align-items: center; justify-content: center; gap: 18px;
    font-family: "Roboto", sans-serif; font-weight: 500; font-size: 18px;
    color: var(--white);
  }
  .contact-item { display: flex; align-items: center; gap: 7px; }
  .contact-icon { width: 20px; height: 20px; }

  /* Front: brand side */
  .card-front { left: 520px; top: 520px; }
  .front-copy {
    position: absolute; inset: 0;
    display: flex; align-items: center; justify-content: center;
    text-align: center;
  }
  .brand-name {
    font-family: "Almendra", serif; font-weight: 400; font-size: 48px;
    color: var(--accent-red);
  }
</style>
</head>
<body>
<main class="canvas">

  <section class="card card-back" aria-label="Appointment card, back side">
    <div class="card-texture" role="img" aria-label="White crumpled paper texture"></div>
    <h1 class="appointment-title">Appointment</h1>
    <div class="field field-name">Name:<span class="field-line"></span></div>
    <div class="field field-at">at:<span class="field-line"></span><span class="meridiem">A.M/P.M</span></div>
    <div class="field field-on">on:<span class="field-line"></span></div>
    <div class="contact-band">
      <span class="contact-item">
        <svg class="contact-icon" viewBox="0 0 20 20" aria-hidden="true">
          <circle cx="10" cy="10" r="10" fill="#ffffff"/>
          <path d="M6.5 5.5l2 0 1 2.5-1.3 1c.6 1.3 1.5 2.2 2.8 2.8l1-1.3 2.5 1v2c0 .6-.5 1-1 1C9.2 14.5 5.5 10.8 5.5 6.5c0-.5.4-1 1-1z" fill="#d8080c"/>
        </svg>
        0491285364
      </span>
      <span class="contact-item">
        <svg class="contact-icon" viewBox="0 0 20 20" aria-hidden="true">
          <circle cx="10" cy="10" r="10" fill="#ffffff"/>
          <rect x="5" y="6.5" width="10" height="7" fill="none" stroke="#d8080c" stroke-width="1.4"/>
          <path d="M5 6.5l5 4 5-4" fill="none" stroke="#d8080c" stroke-width="1.4"/>
        </svg>
        wildplumfolk@postnestmail.net
      </span>
    </div>
  </section>

  <section class="card card-front" aria-label="Brand card, front side">
    <div class="card-texture" role="img" aria-label="White crumpled paper texture"></div>
    <div class="front-copy">
      <p class="brand-name">wild plum folk</p>
    </div>
  </section>

</main>
</body>
</html>
```